Templates for Construction Company

We are looking to have templates prepared for all aspects of our letter sending. Using our brand design. with similar layouts that look the same.

Letterheads design & Email signatures

We use letter heads for - quotes, contract correspondence, variations, formal letters, invitations

Target Market(s)

Clients documents sent in emails

Industry/Entity Type

Construction

Font styles to use
Serif
Sans Serif

Colors
0054AA
0677BA
7BADD7
CADEEF
E8F1F8

Requirements
Must have
• Easy to read, water marks on page
Nice to have
• Different options for different letters

```html
<!DOCTYPE html>
<html lang="en">
<head>
<meta charset="utf-8">
<title>Ironvale Letterhead &amp; Email Signature</title>
<link rel="stylesheet" href="https://fonts.googleapis.com/css2?family=Lato:wght@400;700&family=Lexend:wght@400;500;600&family=Great+Vibes&display=swap">
<style>
  :root {
    --brand-blue: #4d82c8;
    --brand-grey: #555a60;
    --text-grey: #5b5f64;
    --paper: #ffffff;
    --backdrop: #333333;
    --rule: #5b88c9;
    --watermark: #e6e9f1;
  }
  * { box-sizing: border-box; margin: 0; padding: 0; }
  html, body { width: 1200px; height: 1200px; overflow: hidden; }
  body { background: var(--backdrop); position: relative; font-family: "Lato", sans-serif; color: var(--text-grey); }

  .letterhead { position: absolute; left: 293px; top: 60px; width: 613px; height: 836px; background: var(--paper); overflow: hidden; }
  .signature-card { position: absolute; left: 254px; top: 936px; width: 692px; height: 201px; background: var(--paper); overflow: hidden; }

  .abs { position: absolute; }
  .person-name { font-family: "Lexend", sans-serif; font-weight: 500; color: var(--brand-grey); white-space: nowrap; letter-spacing: -0.2px; }
  .person-name .surname { color: var(--brand-blue); }
  .role-tag { background: var(--brand-blue); color: #fff; font-family: "Lato", sans-serif;
    clip-path: polygon(0 0, calc(100% - 12px) 0, 100% 100%, 0 100%); display: flex; align-items: center; }
  .header-rule { height: 1.5px; background: var(--rule); }
  .brand { display: flex; align-items: center; gap: 8px; }
  .brand-square { background: var(--brand-grey); }
  .brand-name { font-family: "Lexend", sans-serif; font-weight: 600; color: var(--brand-blue); line-height: 1; }

  .page-watermark { display: flex; align-items: center; gap: 16px; pointer-events: none; }
  .page-watermark .mark-square { width: 56px; height: 56px; background: var(--watermark); }
  .page-watermark .mark-name { font-family: "Lexend", sans-serif; font-weight: 600; font-size: 92px; line-height: 1; color: var(--watermark); }

  .letter-meta { font-size: 13.5px; top: 187px; }
  .letter-body { left: 37px; width: 536px; font-size: 13.4px; line-height: 18px; text-align: justify; }
  .sign-off { left: 37px; top: 598px; font-size: 13.5px; }
  .signature-name { left: 37px; top: 628px; font-family: "Great Vibes", cursive; font-size: 28px; color: var(--brand-blue); }

  .contact-text { color: #3f4347; white-space: nowrap; }
  .icon { fill: var(--brand-blue); }
  .web-band { background: var(--brand-blue); color: #fff; display: flex; align-items: center; gap: 10px;
    clip-path: polygon(10px 0, 100% 0, 100% 100%, 0 100%); }
</style>
</head>
<body>

<section class="letterhead">
  <div class="abs page-watermark" role="img" aria-label="Faint Ironvale watermark" style="left:120px; top:395px;">
    <span class="mark-square"></span>
    <span class="mark-name">Ironvale</span>
  </div>

  <div class="abs person-name" style="left:37px; top:55px; font-size:22px;">Dana <span class="surname">Whitlock</span></div>
  <div class="abs role-tag" style="left:37px; top:86px; width:116px; height:18px; font-size:12.5px; padding-left:8px;">Consultant</div>
  <div class="abs header-rule" style="left:150px; top:103px; width:255px;"></div>
  <div class="abs brand" style="right:40px; top:72px;">
    <span class="brand-square" style="width:13px; height:13px;"></span>
    <span class="brand-name" style="font-size:32px;">Ironvale</span>
  </div>

  <div class="abs letter-meta" style="left:37px;">Dear Client,</div>
  <div class="abs letter-meta" style="right:40px;">Date: 20.05.2022</div>

  <p class="abs letter-body" style="top:254px;">Lorem ipsum dolor sit amet, consectetur adipiscing elit, sed do eiusmod tempor incididunt ut labore et dolore magna aliqua. Ut enim ad minim veniam, quis nostrud exercitation ullamco laboris nisi ut aliquip ex ea commodo consequat. Excepteur sint occaecat cupidatat non proident, s the readable content of a page when looking at its layout. The point of using Lorem Ipsum is that it has a more-or-less normal distribution of letters, as opposed to using 'Content here, content here', making it look like readable English.</p>
  <p class="abs letter-body" style="top:415px;">Lorem ipsum dolor sit amet, consectetur adipiscing elit, sed do eiusmod tempor incididunt ut labore et dolore magna aliqua.Excepteur sint occaecat cupidatat non proident, sunt in culpa qui officia deserunt mollit anim id est Proident, sunt in culpa qui xcepteur sint occaecat cupidatat officia laborum.</p>
  <p class="abs letter-body" style="top:522px;">Lorem ipsum dolor sit amet, consectetur adipiscing elit, sed do eiusmod tempor incididunt<br>ut labore et dolore magna aliqua.</p>

  <div class="abs sign-off">Sincerely,</div>
  <div class="abs signature-name">Owen Carlisle</div>

  <div class="abs header-rule" style="left:37px; top:731px; width:536px;"></div>

  <svg class="abs icon" style="left:37px; top:751px;" width="12" height="16" viewBox="0 0 12 16" aria-hidden="true"><path d="M6 0C2.7 0 0 2.6 0 5.9 0 10.2 6 16 6 16s6-5.8 6-10.1C12 2.6 9.3 0 6 0zm0 8.3a2.4 2.4 0 1 1 0-4.8 2.4 2.4 0 0 1 0 4.8z"/></svg>
  <div class="abs contact-text" style="left:65px; top:741px; font-size:12.5px; line-height:18px;">418 N. Harbor Lane<br>Suite 220 Fairmont, CA 93011</div>

  <svg class="abs icon" style="left:268px; top:752px;" width="15" height="14" viewBox="0 0 24 24" aria-hidden="true"><path d="M6.6 10.8c1.4 2.8 3.8 5.1 6.6 6.6l2.2-2.2c.3-.3.7-.4 1-.2 1.1.4 2.3.6 3.6.6.6 0 1 .4 1 1V20c0 .6-.4 1-1 1C10.6 21 3 13.4 3 4c0-.6.4-1 1-1h3.5c.6 0 1 .4 1 1 0 1.3.2 2.5.6 3.6.1.3 0 .7-.2 1l-2.3 2.2z"/></svg>
  <div class="abs contact-text" style="left:295px; top:750px; font-size:12.5px;">+1 415 555 0142</div>

  <svg class="abs icon" style="left:441px; top:754px;" width="15" height="11" viewBox="0 0 15 11" aria-hidden="true"><path d="M0 0h15v11H0z M1.2 1.2 7.5 6.2l6.3-5z" fill-rule="evenodd"/></svg>
  <div class="abs contact-text" style="left:467px; top:750px; font-size:12.5px;">hello@ironvale.com</div>

  <div class="abs web-band" style="left:421px; top:785px; width:152px; height:24px; font-size:12.5px; padding-left:17px;">
    <svg width="14" height="14" viewBox="0 0 14 14" aria-hidden="true"><circle cx="7" cy="7" r="6.3" fill="none" stroke="#fff" stroke-width="1.2"/><ellipse cx="7" cy="7" rx="2.6" ry="6.3" fill="none" stroke="#fff" stroke-width="1"/><path d="M0.8 7h12.4" stroke="#fff" stroke-width="1"/></svg>
    <span>www.ironvale.com</span>
  </div>
</section>

<section class="signature-card">
  <div class="abs person-name" style="left:40px; top:25px; font-size:26px;">Dana <span class="surname">Whitlock</span></div>
  <div class="abs role-tag" style="left:40px; top:60px; width:131px; height:22px; font-size:13.5px; padding-left:9px;">Consultant</div>
  <div class="abs header-rule" style="left:168px; top:81px; width:295px;"></div>
  <div class="abs brand" style="right:34px; top:46px;">
    <span class="brand-square" style="width:15px; height:15px;"></span>
    <span class="brand-name" style="font-size:38px;">Ironvale</span>
  </div>

  <svg class="abs icon" style="left:40px; top:114px;" width="13" height="17" viewBox="0 0 12 16" aria-hidden="true"><path d="M6 0C2.7 0 0 2.6 0 5.9 0 10.2 6 16 6 16s6-5.8 6-10.1C12 2.6 9.3 0 6 0zm0 8.3a2.4 2.4 0 1 1 0-4.8 2.4 2.4 0 0 1 0 4.8z"/></svg>
  <div class="abs contact-text" style="left:73px; top:102px; font-size:13.5px; line-height:21px; font-family:'Lexend',sans-serif;">418 N. Harbor Lane<br>Suite 220 Fairmont, CA 93011</div>

  <svg class="abs icon" style="left:306px; top:115px;" width="17" height="16" viewBox="0 0 24 24" aria-hidden="true"><path d="M6.6 10.8c1.4 2.8 3.8 5.1 6.6 6.6l2.2-2.2c.3-.3.7-.4 1-.2 1.1.4 2.3.6 3.6.6.6 0 1 .4 1 1V20c0 .6-.4 1-1 1C10.6 21 3 13.4 3 4c0-.6.4-1 1-1h3.5c.6 0 1 .4 1 1 0 1.3.2 2.5.6 3.6.1.3 0 .7-.2 1l-2.3 2.2z"/></svg>
  <div class="abs contact-text" style="left:336px; top:114px; font-size:13.5px; font-family:'Lexend',sans-serif;">+1 415 555 0142</div>

  <svg class="abs icon" style="left:505px; top:118px;" width="17" height="12" viewBox="0 0 15 11" aria-hidden="true"><path d="M0 0h15v11H0z M1.2 1.2 7.5 6.2l6.3-5z" fill-rule="evenodd"/></svg>
  <div class="abs contact-text" style="left:536px; top:113px; font-size:13.5px; font-family:'Lexend',sans-serif;">hello@ironvale.com</div>

  <div class="abs web-band" style="left:482px; top:148px; width:177px; height:28px; font-size:13.5px; padding-left:20px; font-family:'Lexend',sans-serif;">
    <svg width="16" height="16" viewBox="0 0 14 14" aria-hidden="true"><circle cx="7" cy="7" r="6.3" fill="none" stroke="#fff" stroke-width="1.2"/><ellipse cx="7" cy="7" rx="2.6" ry="6.3" fill="none" stroke="#fff" stroke-width="1"/><path d="M0.8 7h12.4" stroke="#fff" stroke-width="1"/></svg>
    <span>www.ironvale.com</span>
  </div>
</section>

</body>
</html>
```